Moder Business Card Design for Renewables Business

Need a business card design for my business. We collect & repurpose spent coffee ground from cafes. The cards will be made from recycled paper. Needs to fit our corporate colour scheme of white, green & brown (see logo for colour codes). Eco friendly, modern, intresting & eye catching.
This card needs to convey the message of the business and fit into its mantra of eco-friendly, sustainable etc.

Target Market(s)

Cafe Owners, Coffee Drinkers, Recycling Companies, Farmers

Industry/Entity Type

Recycling

Contact Information for Business Card

Name; Peter Dalton
Phone; 0438 216 570
e-mail; info@florivex.com.au
website; www.florivex.com.au

Font styles to use
Sans Serif
Script

Colors

Designer to choose colors to be used in the design.

Requirements
Must have
• FRONT;
• Logo, Name (Peter Dalton), phone number, e-mail address, website
• BACK;
• On the back in cursive text; 'RECLAIMING VALUE FROM EVERY CUP'
• Small facebook & Instagram logos with text 'Florivex'
Should not have
• messy design

```html
<!DOCTYPE html>
<html lang="en">
<head>
<meta charset="utf-8">
<title>Florivex Business Card</title>
<link rel="stylesheet" href="https://fonts.googleapis.com/css2?family=Open+Sans:wght@400;600;700&display=swap">
<style>
  :root {
    --backdrop: #3a3a3c;
    --kraft: #d5c6a5;
    --kraft-light: #ddd0b2;
    --brown: #5b3520;
    --brown-dark: #4a2b19;
    --green: #6f9f4c;
    --ink: #1f1a16;
    --white: #ffffff;
  }
  * { box-sizing: border-box; margin: 0; padding: 0; }
  html, body {
    width: 1200px; height: 1028px; overflow: hidden;
    background: var(--backdrop);
    font-family: "Open Sans", sans-serif;
  }
  .sheet {
    width: 1200px; height: 1028px;
    display: flex; flex-direction: column; align-items: center; justify-content: center;
    gap: 28px;
  }
  .card {
    position: relative;
    width: 840px; height: 480px;
    background: linear-gradient(135deg, var(--kraft-light), var(--kraft));
    box-shadow: 0 10px 24px rgba(0,0,0,0.45);
    overflow: hidden;
  }
  .card__band {
    position: absolute; left: 0; right: 0; bottom: 0;
    background: var(--brown);
  }

  /* Front */
  .front .card__band { height: 64px; }
  .front__mark {
    position: absolute; left: 80px; top: 70px; width: 220px;
    display: flex; flex-direction: column; align-items: center; gap: 18px;
  }
  .mark-ring {
    width: 190px; height: 190px; border-radius: 50%;
    border: 8px solid var(--brown);
  }
  .brand-name {
    font-weight: 700; color: var(--brown); letter-spacing: 1px;
  }
  .front__mark .brand-name { font-size: 34px; }
  .front__divider {
    position: absolute; left: 345px; top: 70px; width: 4px; height: 320px;
    background: var(--brown);
  }
  .front__details { position: absolute; left: 385px; top: 95px; }
  .person-name {
    font-size: 38px; font-weight: 700; text-transform: uppercase; color: var(--ink);
    line-height: 1;
  }
  .person-name .first { color: var(--brown); }
  .person-title {
    margin-top: 8px; font-size: 15px; letter-spacing: 5px; text-transform: uppercase; color: var(--ink);
  }
  .contact-list { list-style: none; margin-top: 34px; display: flex; flex-direction: column; gap: 16px; }
  .contact-item { display: flex; align-items: center; gap: 14px; font-size: 26px; color: var(--ink); }
  .contact-icon {
    width: 34px; height: 34px; border-radius: 7px; background: var(--green);
    display: flex; align-items: center; justify-content: center; flex-shrink: 0;
  }

  /* Back */
  .back .card__band { height: 140px; padding: 26px 0 0 150px; display: flex; flex-direction: column; gap: 16px; }
  .back__mark {
    position: absolute; left: 0; right: 0; top: 40px;
    display: flex; flex-direction: column; align-items: center; gap: 14px;
  }
  .back__mark .mark-ring { width: 170px; height: 170px; }
  .back__mark .brand-name { font-size: 46px; color: var(--green); letter-spacing: 2px; text-transform: uppercase; }
  .tagline {
    position: absolute; right: 40px; bottom: 152px;
    font-size: 22px; font-weight: 700; text-transform: uppercase; color: var(--brown-dark);
  }
  .social-item { display: flex; align-items: center; gap: 16px; font-size: 26px; color: var(--white); }
  .social-dot { width: 30px; height: 30px; border-radius: 50%; border: 3px solid var(--white); }
</style>
</head>
<body>
<main class="sheet">

  <section class="card front" aria-label="Business card front">
    <div class="front__mark">
      <div class="mark-ring"></div>
      <span class="brand-name">Florivex</span>
    </div>
    <div class="front__divider"></div>
    <div class="front__details">
      <h1 class="person-name"><span class="first">Peter</span> Dalton</h1>
      <p class="person-title">Managing Director</p>
      <ul class="contact-list">
        <li class="contact-item">
          <span class="contact-icon">
            <svg width="20" height="20" viewBox="0 0 24 24"><path fill="#fff" d="M6.6 10.8a15 15 0 0 0 6.6 6.6l2.2-2.2c.3-.3.7-.4 1-.2 1.1.4 2.3.6 3.6.6.6 0 1 .4 1 1V20c0 .6-.4 1-1 1A17 17 0 0 1 3 4c0-.6.4-1 1-1h3.5c.6 0 1 .4 1 1 0 1.3.2 2.5.6 3.6.1.3 0 .7-.2 1z"/></svg>
          </span>
          0438 216 570
        </li>
        <li class="contact-item">
          <span class="contact-icon">
            <svg width="20" height="20" viewBox="0 0 24 24"><rect x="3" y="6" width="18" height="12" rx="1.5" fill="#fff"/><path d="M3.5 6.5 12 13l8.5-6.5" fill="none" stroke="#6f9f4c" stroke-width="1.8"/></svg>
          </span>
          info@florivex.com.au
        </li>
        <li class="contact-item">
          <span class="contact-icon">
            <svg width="20" height="20" viewBox="0 0 24 24" fill="none" stroke="#fff" stroke-width="1.8"><circle cx="12" cy="12" r="9"/><ellipse cx="12" cy="12" rx="4" ry="9"/><path d="M3 12h18M5 7h14M5 17h14"/></svg>
          </span>
          www.florivex.com.au
        </li>
      </ul>
    </div>
    <div class="card__band"></div>
  </section>

  <section class="card back" aria-label="Business card back">
    <div class="back__mark">
      <div class="mark-ring"></div>
      <span class="brand-name">Florivex</span>
    </div>
    <p class="tagline">Reclaiming value from every cup</p>
    <div class="card__band">
      <div class="social-item"><span class="social-dot"></span>friendpage.com/florivex</div>
      <div class="social-item"><span class="social-dot"></span>photogram.com/florivex</div>
    </div>
  </section>

</main>
</body>
</html>
```